Travel video blogger needs website design

I need a website designed for my new travel video blog "Roaming Sparrow". I have only just started but need a website that is fairly simple and not too busy. I have a logo which I want on it (I have attached it to this project). I also want a link to all my other social medias on the main page (vidtrekhub, Snapwell and Palnook) and my videos as well. Here is a link to my vidtrekhub page for you to look at: https://www.vidtrekhub.net/channel/QRm4tZ8pWnE2HX57YKccd31v
As I have only just started and I am still trying to find my specific niche, again I need it to be sleek and simple that I can go in and change slightly here and there. I would like these pages on the website: About Me, Videos, Social Media, Blog, Gallery, contact me. for an example I like the look of www.theroamingkinfolk.net website.

I already have the domain and I am with Harborweb with pagecraftr.org. I just want to spend my time getting better and learning about videos then trying to create a website (I am a bit of a perfectionist when I try to do something).

Target Market(s)

Young Adults (majority females) between the ages of 18 and 30 with an interest in travelling.

Industry/Entity Type

Travel Industry

Number of Pages Required

1 page

Colors

Designer to choose colors to be used in the design.

Requirements
Must have
• A like to my Snapwell, Palnook and vidtrekhub channels on the home page
• Must be a nice, simple design
• Must have my logo on the front and name "Roaming Sparrow"
Nice to have
• A nice light, bright coloured theme
Should not have
• A dark coloured theme

```html
<!DOCTYPE html>
<html lang="en">
<head>
<meta charset="UTF-8">
<title>Roaming Sparrow — Featured Posts</title>
<link rel="stylesheet" href="https://fonts.googleapis.com/css2?family=Raleway:wght@600;700&family=Roboto:wght@400&display=swap">
<style>
  :root {
    --ink: #222222;
    --paper: #ffffff;
    --rule: #c9c9c9;
    --accent: #2ecc8f;
    --white: #ffffff;
    --shade: rgba(0, 0, 0, 0.45);
  }
  * { margin: 0; padding: 0; box-sizing: border-box; }
  html, body { width: 1200px; height: 587px; overflow: hidden; background: var(--paper); }
  body { position: relative; font-family: "Raleway", sans-serif; color: var(--ink); }

  .frame-top { position: absolute; left: 0; top: 1px; width: 1200px; height: 1px; background: var(--rule); }
  .frame-right { position: absolute; left: 1199px; top: 0; width: 1px; height: 587px; background: #d8d8d8; }
  .frame-foot { position: absolute; left: 0; top: 585px; width: 43px; height: 2px; background: #1f3a3a; }

  .section-title {
    position: absolute; left: 0; top: 3px; width: 1200px; text-align: center;
    font-size: 20px; font-weight: 700; letter-spacing: 0.2px; text-transform: uppercase;
  }

  .featured { position: absolute; left: 162px; top: 53px; display: flex; gap: 4px; }
  .featured-post { width: 172px; text-align: center; }
  .featured-thumb { width: 172px; height: 231px; }
  .featured-name { margin-top: 17px; font-size: 18px; font-weight: 600; line-height: 23px; padding: 0 20px; }

  .thumb-maldives { background: linear-gradient(180deg, #e9e7e6 0%, #dcdcda 45%, #9fb2b4 62%, #b48a58 80%, #8c6136 100%); }
  .thumb-dubai { background: linear-gradient(180deg, #9f9ef2 0%, #a4a3f5 60%, #7f80dc 100%); }
  .thumb-australia { background: linear-gradient(180deg, #050507 0%, #0b1330 35%, #2f5fd6 55%, #0e1a55 75%, #141a48 100%); }
  .thumb-greece { background: linear-gradient(180deg, #d8e6f0 0%, #cbdce8 40%, #e8e8e8 65%, #a9a9a4 100%); }
  .thumb-traveler { background: linear-gradient(160deg, #6e6a3e 0%, #8e8a78 35%, #3f5a80 60%, #4e4f55 100%); }

  .divider { position: absolute; left: 555px; top: 403px; width: 89px; height: 2px; background: var(--accent); }

  .card { position: absolute; top: 494px; width: 275px; height: 110px; overflow: hidden; }
  .card-photo { left: 160px; background: linear-gradient(180deg, #3a3230 0%, #5b4d44 40%, #2a2523 100%); }
  .card-quote { left: 461px; background: linear-gradient(180deg, #4a4c44 0%, #3a3c36 100%); }
  .card-video { left: 763px; background: linear-gradient(180deg, #3d5f7a 0%, #6f8f6a 50%, #3f6f95 100%); }

  .quote-mark { position: absolute; left: 18px; top: 17px; width: 18px; height: 15px; }
  .quote-text {
    position: absolute; left: 50px; top: 56px; color: var(--white);
    font-size: 26px; font-weight: 700; white-space: nowrap;
  }

  .video-bar { position: absolute; left: 0; top: 0; width: 100%; height: 44px; background: linear-gradient(180deg, var(--shade), transparent); }
  .video-title {
    position: absolute; left: 14px; top: 12px; width: 186px; color: var(--white);
    font-family: "Roboto", sans-serif; font-size: 15px; white-space: nowrap; overflow: hidden;
  }
  .video-icon { position: absolute; top: 12px; width: 18px; height: 18px; }
  .icon-clock { left: 210px; }
  .icon-share { left: 242px; }
  .video-play { position: absolute; left: 117px; top: 70px; width: 42px; height: 42px; }

  .to-top {
    position: absolute; left: 1154px; top: 551px; width: 44px; height: 34px;
    border: 1px solid var(--accent); background: var(--paper);
  }
  .to-top svg { position: absolute; left: 6px; top: 1px; }
</style>
</head>
<body>
  <div class="frame-top"></div>
  <div class="frame-right"></div>
  <div class="frame-foot"></div>

  <h2 class="section-title">Featured Posts</h2>

  <div class="featured">
    <article class="featured-post">
      <div class="featured-thumb thumb-maldives" role="img" aria-label="Wooden jetty leading to a thatched hut over calm sea"></div>
      <h3 class="featured-name">Maldives</h3>
    </article>
    <article class="featured-post">
      <div class="featured-thumb thumb-dubai" role="img" aria-label="Tall skyscraper against a violet sky with a plane"></div>
      <h3 class="featured-name">Dubai</h3>
    </article>
    <article class="featured-post">
      <div class="featured-thumb thumb-australia" role="img" aria-label="Opera house lit blue at night over the harbour"></div>
      <h3 class="featured-name">Australia</h3>
    </article>
    <article class="featured-post">
      <div class="featured-thumb thumb-greece" role="img" aria-label="White island village with a windmill"></div>
      <h3 class="featured-name">Lorem Ipsum Dolor</h3>
    </article>
    <article class="featured-post">
      <div class="featured-thumb thumb-traveler" role="img" aria-label="Traveller with backpack seen from behind on a city street"></div>
      <h3 class="featured-name">Hello world!</h3>
    </article>
  </div>

  <div class="divider"></div>

  <div class="card card-photo" role="img" aria-label="Narrow street between old brick buildings"></div>

  <div class="card card-quote" role="img" aria-label="Quote over a dark mountain landscape">
    <svg class="quote-mark" viewBox="0 0 18 15" aria-hidden="true">
      <path fill="#ffffff" d="M0 8 Q0 1 7 0 V3 Q3 4 3 7 H7 V15 H0 Z M11 8 Q11 1 18 0 V3 Q14 4 14 7 H18 V15 H11 Z"/>
    </svg>
    <p class="quote-text">“For my part, I</p>
  </div>

  <div class="card card-video" role="img" aria-label="Video thumbnail of friends overlooking a green valley">
    <div class="video-bar"></div>
    <p class="video-title">2 Years on the Road in 4 Mi...</p>
    <svg class="video-icon icon-clock" viewBox="0 0 18 18" aria-hidden="true">
      <circle cx="9" cy="9" r="9" fill="#ffffff"/>
      <path d="M9 4 V9 L12 11" stroke="#333" stroke-width="1.6" fill="none"/>
    </svg>
    <svg class="video-icon icon-share" viewBox="0 0 18 18" aria-hidden="true">
      <path fill="#ffffff" d="M10 3 L18 9 L10 15 V11 Q3 11 0 16 Q1 7 10 7 Z"/>
    </svg>
    <svg class="video-play" viewBox="0 0 42 42" aria-hidden="true">
      <circle cx="21" cy="21" r="21" fill="rgba(20,20,20,0.8)"/>
      <path d="M16 13 L30 21 L16 29 Z" fill="#ffffff"/>
    </svg>
  </div>

  <a class="to-top" href="#" aria-label="Back to top">
    <svg width="31" height="31" viewBox="0 0 31 31" aria-hidden="true">
      <circle cx="15.5" cy="15.5" r="15.5" fill="#2ecc8f"/>
      <path d="M8 16 L15.5 9 L23 16 M8 23 L15.5 16 L23 23" stroke="#ffffff" stroke-width="3.2" fill="none" stroke-linejoin="miter"/>
    </svg>
  </a>
</body>
</html>
```